Compelling Home Page for Clip Reach Forge

We are a Video SEO specialist that get websites on top of the front page of Searvo and ClipTube with video thumbprints that generate great traffic. Video SEO is all we do

see what we're offering at a salespage www.bringmoreclipviews.example. However, please omit "guarantee"

he home page should introduce our company as a premier company for helping brands get their videos on the front page of searvo and high up in cliptube. Should incorporate video "thumbnails" as part of the design. These could be the "triangular click buttons" or little video screens you see as "thumbnails" Needs a prominent place for a video about videoSEO. on Left side of page towards the top.

Needs buttons across the top for other pages. See www.toprankclips.example for frame of reference we want to be better than them.

Must incorporate our logo. We'd like to see the logo on dark background as well as white background.

Simple but with bright and vibrant highlights that look sophisticated, cutting edge and accountable. Shows credentials. Links with examples of thumbnails that are on the front page

We want to beat www.toprankclips.example check it out for point of reference

Target Market(s)

large corporations who have videos already and want to get better traction. Summit 1000. Advertising Agencies for Summit 1000's

Requirements
Must have
• Incorporate our logo. clean, easy to read

```html
<!DOCTYPE html>
<html lang="en">
<head>
<meta charset="utf-8">
<title>Clip Reach Forge — Video SEO</title>
<link href="https://fonts.googleapis.com/css2?family=Arimo:wght@400;700&display=swap" rel="stylesheet">
<style>
:root{
  --wine:#8e3a4a;
  --wine-light:#b86674;
  --night:#0c1b22;
  --page:#ececec;
  --panel:#f6f6f6;
  --line:#d8d8d8;
  --ink:#4a4a4a;
  --ink-soft:#5c5c5c;
  --accent:#e0344f;
  --link:#1fa3d6;
  --gold:#f5a623;
}
*{box-sizing:border-box;margin:0;padding:0}
html,body{width:1200px;height:1200px;overflow:hidden}
body{position:relative;font-family:"Arimo",Arial,sans-serif;color:var(--ink);
  background:linear-gradient(#fff 442px,var(--page) 520px,var(--page))}
.hero-band{position:absolute;left:0;top:0;width:1200px;height:380px;
  background:linear-gradient(160deg,#7a2f3f 0%,#b35d6d 30%,#8c3949 60%,#7e3040 100%)}
.dark-band{position:absolute;left:0;top:380px;width:1200px;height:62px;background:var(--night)}
.topbar{position:absolute;left:0;top:0;width:1200px;height:42px;border-bottom:1px solid rgba(255,255,255,.18);
  color:#fff;font-size:10px}
.topbar .follow{position:absolute;left:190px;top:16px;display:flex;gap:4px;align-items:center}
.topbar .follow i{display:inline-block;width:12px;height:12px;border-radius:2px;margin-left:3px}
.support{position:absolute;left:611px;top:16px}
.search{position:absolute;left:853px;top:10px;width:156px;height:22px;background:#fff;border:1px solid #ccc;border-radius:3px;
  font-size:10px;color:#333;padding:5px 7px}
.search .go{position:absolute;right:2px;top:2px;width:18px;height:16px;background:#1e5c73;border-radius:2px}
.brand{position:absolute;left:198px;top:48px;display:flex;align-items:center;gap:8px;color:#fff;font-size:21px}
.brand .dot{width:56px;height:56px;border-radius:50%;background:var(--gold)}
.nav{position:absolute;left:642px;top:81px;display:flex;font-size:10px;color:#fff}
.nav a{color:#fff;text-decoration:none;width:72px;height:26px;line-height:26px;text-align:center}
.nav a.active{width:67px;background:linear-gradient(#e65a70,#c8223d);border-radius:3px;margin-right:8px}
.nav a+a{margin-left:2px}
.rule{position:absolute;left:189px;top:141px;width:822px;border-top:1px solid rgba(255,255,255,.25)}
.slider{position:absolute;left:187px;top:148px;width:826px;height:380px;background:#e6e6e6;border:1px solid #cfcfcf;padding:5px}
.slider .scene{position:relative;width:100%;height:100%;
  background:linear-gradient(180deg,#3b3f6d 0%,#5a5f8e 35%,#6b6d8a 55%,#a89a7a 80%,#6a5f4d 100%)}
.slide-title{position:absolute;left:500px;top:168px;font-size:44px;color:rgba(40,40,40,.45)}
.slide-copy{position:absolute;left:385px;top:230px;width:365px;font-size:8px;line-height:17px;color:rgba(230,230,230,.6);text-align:right}
.play{position:absolute;left:22px;top:318px}
.sound{position:absolute;left:737px;top:322px}
.welcome{position:absolute;left:189px;top:543px;width:822px;height:137px;background:var(--panel);border:1px solid var(--line)}
h2{font-weight:400;font-size:20px;color:var(--ink)}
.welcome h2{position:absolute;left:17px;top:17px}
.glyph{position:absolute;width:46px;height:50px;border-radius:8px}
.welcome .glyph{left:23px;top:58px;background:linear-gradient(#e8a35a,#a95a1e)}
.copy{position:absolute;font-size:10.5px;line-height:17px;color:var(--ink-soft)}
.welcome .copy{left:89px;top:61px;width:700px}
.download h2{position:absolute;left:207px;top:694px}
.download .glyph{left:210px;top:742px;background:linear-gradient(#c56a2a,#8b3e12)}
.download .copy{left:279px;top:740px;width:690px}
.shade{position:absolute;left:189px;top:818px;width:822px;height:14px;
  background:radial-gradient(ellipse at top,rgba(0,0,0,.08),transparent 70%)}
.col{position:absolute;top:858px;width:250px}
.col h3{font-weight:400;font-size:15.5px;color:var(--ink)}
.col .sub{font-size:9px;color:var(--link);margin-top:6px}
.col .thumb{margin-top:17px;height:70px;border:4px solid #dcdcdc;outline:1px solid #c8c8c8;
  display:flex;align-items:center;justify-content:center;font-size:22px}
.col p{font-size:10.5px;line-height:17px;color:var(--ink-soft);margin-top:17px}
.col .more{font-size:10.5px;font-weight:700;color:var(--ink);margin-top:1px;display:block}
.thumb.pink{background:linear-gradient(120deg,#fbe0ea,#f0a8c2);color:#7a6a70}
.thumb.green{background:linear-gradient(120deg,#9bd23a,#5ea815);color:#eaffd0;font-size:15px}
.thumb.blue{background:linear-gradient(120deg,#1a4fb5,#3d8be0);color:#d8e8ff}
.footer{position:absolute;left:0;top:1148px;width:1200px;height:52px;background:linear-gradient(#0f1f26,#0a171c)}
.footer .brand{top:10px;left:193px;font-size:21px}
.footer .brand .dot{width:34px;height:34px}
.footer .legal{position:absolute;left:726px;top:14px;font-size:9.5px;color:#ddd}
</style>
</head>
<body>
<div class="hero-band"></div>
<div class="dark-band"></div>

<header class="topbar">
  <div class="follow">Follow us on social network
    <i style="background:#f08a24"></i><i style="background:#4466aa"></i><i style="background:#5ab6e6"></i></div>
  <div class="support">Click here to live Support &nbsp;Tell Free 1-555-010-2040</div>
  <div class="search">Search<span class="go"></span></div>
</header>

<div class="brand"><span class="dot"></span>Clip Reach Forge</div>

<nav class="nav">
  <a class="active" href="#">Home</a><a href="#">Services</a><a href="#">Order</a><a href="#">Contact Us</a>
</nav>
<div class="rule"></div>

<section class="slider">
  <div class="scene" role="img" aria-label="Night city skyline with glowing skyscrapers and light trails">
    <div class="slide-title">Trend Social</div>
    <div class="slide-copy">Lorem ipsum dolor sit amet, consectetur adipiscing elit. Integer vitae nibh, ultrices et rhoncus at, amet lorem rutrum augue. Morbi sit amet ante vitae, lobortis elementum vitae, placerat a justo.</div>
    <svg class="play" width="54" height="54" viewBox="0 0 54 54">
      <circle cx="27" cy="27" r="26" fill="#f2f2f2" stroke="#bbb"/>
      <circle cx="27" cy="27" r="21" fill="#dcdde6"/>
      <path d="M17 17 L42 27 L17 37 L22 27 Z" fill="#1b1f6e"/>
    </svg>
    <svg class="sound" width="54" height="46" viewBox="0 0 54 46">
      <path d="M2 15 H12 L26 3 V43 L12 31 H2 Z" fill="#14146e"/>
      <path d="M32 14 Q38 23 32 32" stroke="#14146e" stroke-width="4" fill="none"/>
      <path d="M38 9 Q47 23 38 37" stroke="#14146e" stroke-width="4" fill="none"/>
      <path d="M44 4 Q56 23 44 42" stroke="#14146e" stroke-width="4" fill="none"/>
    </svg>
  </div>
</section>

<section class="welcome">
  <h2>Welcome to Clip Reach Forge</h2>
  <div class="glyph" role="img" aria-label="Clipboard with pen icon"></div>
  <p class="copy">Lorem ipsum dolor sit amet, consectetur adipiscing elit. Pellentesque diam ligula, egestas eget rhoncus vel, hendrerit in sem. Vivamus laoreet erat sit amet ante ullamcorper vestibulum. Duis porta, nisl sed cursus volutpat, est nulla placerat mauris, id viverra leo ante sed leo. Vivamus fermentum dignissim sem, quis pellentesque dolor posuere vel. In vitae lorem ligula, a congue nibh.</p>
</section>

<section class="download">
  <h2>Download Free Videos</h2>
  <div class="glyph" role="img" aria-label="Wooden crate with green download arrow icon"></div>
  <p class="copy">Ad malorum ceteros percipitur duo, no alii eros copiosae ius, ius nostrud offendit accommodare at. Everti facilis singulis eam no, vis quaestio consetetur nod malorum ceteros percipitur duo, no alii eros copiosae ius, ius nostrud offendit accommodare at. Everti facilis singulis eam no, vis quaestio consetetur</p>
</section>
<div class="shade"></div>

<article class="col" style="left:207px">
  <h3>Establish social media presence</h3>
  <div class="sub">Sed congue, dui vel tristique mollis...</div>
  <div class="thumb pink" role="img" aria-label="Soft pink banner">Social Media Presence</div>
  <p>Lorem ipsum dolor sit amet, consectetuer adipiscing elit. Aenean commodo ligula eget dolor. Aenean massa. Cum sociis natoque penatibus et magnis dis parturient montes, nascetur ridiculus mus.</p>
  <a class="more" href="#">read more »</a>
</article>
<article class="col" style="left:477px">
  <h3>Media management and advertising</h3>
  <div class="sub">Sed congue, dui vel tristique mollis...</div>
  <div class="thumb green" role="img" aria-label="Green leaf with water drops banner">Media Management Advertising</div>
  <p>Aenean massa. Cum sociis natoque penatibus et magnis dis parturient montes, nascetur ridiculus mus. Donec quam felis, ultricies nec, pellentesque eu, pretium quis, sem. Nulla consequat massa quis enim.</p>
  <a class="more" href="#">read more »</a>
</article>
<article class="col" style="left:747px">
  <h3>Analyze and engage</h3>
  <div class="sub">Sed congue, dui vel tristique mollis...</div>
  <div class="thumb blue" role="img" aria-label="Blue swoosh banner">Analize And Engage</div>
  <p>Lorem ipsum dolor sit amet, consectetur adipiscing elit. Pellentesque diam ligula, egestas eget rhoncus vel, hendrerit in sem. Vivamus laoreet erat sit amet ante ullamcorper vestibulum. Duis porta, nisl sed cursus volutpat, est nulla placerat mauris, id viverra leo ante sed leo.</p>
  <a class="more" href="#">read more »</a>
</article>

<footer class="footer">
  <div class="brand"><span class="dot"></span>Clip Reach Forge</div>
  <div class="legal">© Copyright Clip Reach Forge . All Rights Reserved Home | Contact | RSS</div>
</footer>
</body>
</html>
```